Kinsmen Crest Beard Oil Label for 1oz dropper bottle

Create a label for a 1oz beard oil dropper bottle. The label is 1.5 inches tall and 2.75 inches wide. Our logo is listed in the brief so please use it but it doesnt have to be that prominent. BEARD OIL is the most important verbiage. We like elements of all the attached images but we want our own look and feel.

Target Market(s)

Men with beards

Requirements
Must have
• Kinsmen Crest Logo, BEARD OIL, Flavor (Tobacco Vanilla)

Ingredients
Fractionated Coconut Oil (MCT)
Golden Jojoba Oil
Hemp Seed Oil
Tea Tree Essential Oil
Orange Bitter Essential Oil
Peppermint Supreme Essential Oil
Tallow Aromas
DYE FREE

Directions:
Directions: apply 3-6 drops into your hand...rub oil into hands and apply directly onto beard. For best results massage into skin under beard area and work oil out towards beard. Discontinue use if skin becomes irritated.

100% MADE IN THE USA (American Flag 1 color)
Veteran Owned Co.
Nice to have
• Labels can change color with each flavor or a ring can change color to show flavor.

```html
<!DOCTYPE html>
<html lang="en">
<head>
<meta charset="utf-8">
<title>Kinsmen Crest Beard Oil – Label Colourways</title>
<link href="https://fonts.googleapis.com/css2?family=Montserrat:wght@800;900&family=Exo+2:wght@300&family=Archivo:wght@400;700&display=swap" rel="stylesheet">
<style>
  :root{
    --sheet:#b6bcb3;
    --ink:#ffffff;
    --flavor-ink:#ece2b8;
    --accent-red:#bf4553;
    --kraft:#b39670;
    --kraft-dark:#8c7150;
    --gold:#c9a443;
    --tag-black:#0d0b0a;
    --flag-red:#c8323c;
    --flag-blue:#2b3a78;
  }
  *{margin:0;padding:0;box-sizing:border-box}
  html,body{width:1200px;height:1200px;overflow:hidden}
  body{background:var(--sheet);position:relative;font-family:"Archivo",sans-serif}

  .label{position:absolute;width:500px;height:273px;overflow:hidden;background:var(--base);color:var(--ink)}
  .label--purple{--base:#3f3a5a;--red:var(--accent-red);left:65px;top:52px}
  .label--rust{--base:#9a4327;--red:#c4533f;left:635px;top:52px}
  .label--olive{--base:#5d5434;--red:var(--accent-red);left:65px;top:417px}
  .label--plum{--base:#7b2a49;--red:#c03e58;left:635px;top:417px}
  .label--forest{--base:#3c5948;--red:var(--accent-red);left:65px;top:782px}

  .label__band{position:absolute;inset:0;width:500px;height:273px}
  .label__artwork{position:absolute;left:129px;top:110px;width:253px;height:163px;
    background:radial-gradient(ellipse at 45% 70%, #4a3d30 0%, #6d5a45 28%, transparent 55%),
               linear-gradient(160deg,var(--kraft) 0%,var(--kraft-dark) 100%)}
  .label__usa-box{position:absolute;left:382px;top:174px;width:118px;height:82px;background:var(--base)}
  .label__gold-strip{position:absolute;left:325px;top:256px;width:175px;height:17px;background:var(--gold)}

  .label__size{position:absolute;left:11px;top:29px;font-family:"Montserrat",sans-serif;font-weight:800;font-size:16px;letter-spacing:1px;white-space:nowrap}
  .label__brand{position:absolute;left:155px;top:10px;width:119px;text-align:center;font-weight:700;font-size:17px;line-height:19px;letter-spacing:1px;text-transform:uppercase}
  .label__veteran{position:absolute;left:280px;top:30px;font-family:"Montserrat",sans-serif;font-weight:800;font-size:11.5px;white-space:nowrap}
  .label__title{position:absolute;left:84px;top:60px;font-family:"Montserrat",sans-serif;font-weight:900;font-size:47px;letter-spacing:-0.5px;line-height:1;text-shadow:3px 3px 0 var(--tag-black);white-space:nowrap}
  .label__flavor{position:absolute;left:205px;top:104px;width:186px;height:33px;background:var(--tag-black);border:1px solid #f2ecd8;
    font-family:"Exo 2",sans-serif;font-weight:300;font-size:21.5px;color:var(--flavor-ink);line-height:31px;text-align:center;white-space:nowrap}

  .label__heading{position:absolute;font-size:9px;text-decoration:underline;text-transform:uppercase;white-space:nowrap}
  .label__heading--ingredients{left:4px;top:89px}
  .label__heading--directions{right:8px;top:5px}
  .label__ingredients{position:absolute;left:4px;top:112px;font-size:9px;line-height:12.2px;white-space:nowrap}
  .label__dye{position:absolute;left:4px;top:221px;font-size:9px}
  .label__directions{position:absolute;right:8px;top:29px;font-size:9px;line-height:12.2px;text-align:right;white-space:nowrap}
  .label__origin{position:absolute;left:382px;top:189px;width:118px;text-align:center;font-weight:700;font-size:9px;line-height:12.2px}
  .label__flag{position:absolute;left:435px;top:222px;width:22px;height:22px}
</style>
</head>
<body>

<section class="label label--purple">
  <svg class="label__band" viewBox="0 0 500 273"><polygon points="284,0 500,0 500,174 205,174" fill="var(--red)"/></svg>
  <div class="label__artwork" role="img" aria-label="Engraved portrait of a bearded man in a brimmed hat on kraft paper"></div>
  <div class="label__usa-box"></div>
  <div class="label__gold-strip"></div>
  <div class="label__size">~ 1 OZ ~</div>
  <div class="label__brand">Kinsmen<br>Crest</div>
  <div class="label__veteran">Veteran Owned Co.</div>
  <div class="label__heading label__heading--directions">Directions:</div>
  <p class="label__directions">APPLY 3-6 DROPS<br>INTO YOUR<br>HAND...RUB OIL INTO<br>HANDS AND APPLY<br>DIRECTLY ONTO<br>BEARD. FOR BEST<br>RESULTS MASSAGE<br>INTO SKIN UNDER<br>BEARD AREA AND<br>WORK OIL OUT TO-<br>WARDS BEARD. DIS-</p>
  <h1 class="label__title">BEARD OIL</h1>
  <div class="label__flavor">Tobacco Vanilla</div>
  <div class="label__heading label__heading--ingredients">Ingredients:</div>
  <p class="label__ingredients">FRACTIONATED COCONUT<br>OIL (MCT), GOLDEN<br>JOJOBA OIL. HEMP SEED<br>OIL, TEA TREE ESSENTIAL<br>OIL, ORANGE BITTER<br>ESSENTIAL OIL, PEPPER-<br>MINT SUPREME ESSENTIAL<br>OIL, TALLOW AROMAS.</p>
  <div class="label__dye">DYE FREE</div>
  <p class="label__origin">100%<br>MADE IN THE USA</p>
  <svg class="label__flag" viewBox="0 0 24 24"><defs><clipPath id="c1"><circle cx="12" cy="12" r="12"/></clipPath></defs><g clip-path="url(#c1)"><rect width="24" height="24" fill="#fff"/><rect y="0" width="24" height="3" fill="var(--flag-red)"/><rect y="6" width="24" height="3" fill="var(--flag-red)"/><rect y="12" width="24" height="3" fill="var(--flag-red)"/><rect y="18" width="24" height="3" fill="var(--flag-red)"/><rect width="11" height="12" fill="var(--flag-blue)"/></g></svg>
</section>

<section class="label label--rust">
  <svg class="label__band" viewBox="0 0 500 273"><polygon points="284,0 500,0 500,174 205,174" fill="var(--red)"/></svg>
  <div class="label__artwork" role="img" aria-label="Engraved portrait of a bearded man in a brimmed hat on kraft paper"></div>
  <div class="label__usa-box"></div>
  <div class="label__gold-strip"></div>
  <div class="label__size">~ 1 OZ ~</div>
  <div class="label__brand">Kinsmen<br>Crest</div>
  <div class="label__veteran">Veteran Owned Co.</div>
  <div class="label__heading label__heading--directions">Directions:</div>
  <p class="label__directions">APPLY 3-6 DROPS<br>INTO YOUR<br>HAND...RUB OIL INTO<br>HANDS AND APPLY<br>DIRECTLY ONTO<br>BEARD. FOR BEST<br>RESULTS MASSAGE<br>INTO SKIN UNDER<br>BEARD AREA AND<br>WORK OIL OUT TO-<br>WARDS BEARD. DIS-</p>
  <h1 class="label__title">BEARD OIL</h1>
  <div class="label__flavor">Tobacco Vanilla</div>
  <div class="label__heading label__heading--ingredients">Ingredients:</div>
  <p class="label__ingredients">FRACTIONATED COCONUT<br>OIL (MCT), GOLDEN<br>JOJOBA OIL. HEMP SEED<br>OIL, TEA TREE ESSENTIAL<br>OIL, ORANGE BITTER<br>ESSENTIAL OIL, PEPPER-<br>MINT SUPREME ESSENTIAL<br>OIL, TALLOW AROMAS.</p>
  <div class="label__dye">DYE FREE</div>
  <p class="label__origin">100%<br>MADE IN THE USA</p>
  <svg class="label__flag" viewBox="0 0 24 24"><defs><clipPath id="c2"><circle cx="12" cy="12" r="12"/></clipPath></defs><g clip-path="url(#c2)"><rect width="24" height="24" fill="#fff"/><rect y="0" width="24" height="3" fill="var(--flag-red)"/><rect y="6" width="24" height="3" fill="var(--flag-red)"/><rect y="12" width="24" height="3" fill="var(--flag-red)"/><rect y="18" width="24" height="3" fill="var(--flag-red)"/><rect width="11" height="12" fill="var(--flag-blue)"/></g></svg>
</section>

<section class="label label--olive">
  <svg class="label__band" viewBox="0 0 500 273"><polygon points="284,0 500,0 500,174 205,174" fill="var(--red)"/></svg>
  <div class="label__artwork" role="img" aria-label="Engraved portrait of a bearded man in a brimmed hat on kraft paper"></div>
  <div class="label__usa-box"></div>
  <div class="label__gold-strip"></div>
  <div class="label__size">~ 1 OZ ~</div>
  <div class="label__brand">Kinsmen<br>Crest</div>
  <div class="label__veteran">Veteran Owned Co.</div>
  <div class="label__heading label__heading--directions">Directions:</div>
  <p class="label__directions">APPLY 3-6 DROPS<br>INTO YOUR<br>HAND...RUB OIL INTO<br>HANDS AND APPLY<br>DIRECTLY ONTO<br>BEARD. FOR BEST<br>RESULTS MASSAGE<br>INTO SKIN UNDER<br>BEARD AREA AND<br>WORK OIL OUT TO-<br>WARDS BEARD. DIS-</p>
  <h1 class="label__title">BEARD OIL</h1>
  <div class="label__flavor">Tobacco Vanilla</div>
  <div class="label__heading label__heading--ingredients">Ingredients:</div>
  <p class="label__ingredients">FRACTIONATED COCONUT<br>OIL (MCT), GOLDEN<br>JOJOBA OIL. HEMP SEED<br>OIL, TEA TREE ESSENTIAL<br>OIL, ORANGE BITTER<br>ESSENTIAL OIL, PEPPER-<br>MINT SUPREME ESSENTIAL<br>OIL, TALLOW AROMAS.</p>
  <div class="label__dye">DYE FREE</div>
  <p class="label__origin">100%<br>MADE IN THE USA</p>
  <svg class="label__flag" viewBox="0 0 24 24"><defs><clipPath id="c3"><circle cx="12" cy="12" r="12"/></clipPath></defs><g clip-path="url(#c3)"><rect width="24" height="24" fill="#fff"/><rect y="0" width="24" height="3" fill="var(--flag-red)"/><rect y="6" width="24" height="3" fill="var(--flag-red)"/><rect y="12" width="24" height="3" fill="var(--flag-red)"/><rect y="18" width="24" height="3" fill="var(--flag-red)"/><rect width="11" height="12" fill="var(--flag-blue)"/></g></svg>
</section>

<section class="label label--plum">
  <svg class="label__band" viewBox="0 0 500 273"><polygon points="284,0 500,0 500,174 205,174" fill="var(--red)"/></svg>
  <div class="label__artwork" role="img" aria-label="Engraved portrait of a bearded man in a brimmed hat on kraft paper"></div>
  <div class="label__usa-box"></div>
  <div class="label__gold-strip"></div>
  <div class="label__size">~ 1 OZ ~</div>
  <div class="label__brand">Kinsmen<br>Crest</div>
  <div class="label__veteran">Veteran Owned Co.</div>
  <div class="label__heading label__heading--directions">Directions:</div>
  <p class="label__directions">APPLY 3-6 DROPS<br>INTO YOUR<br>HAND...RUB OIL INTO<br>HANDS AND APPLY<br>DIRECTLY ONTO<br>BEARD. FOR BEST<br>RESULTS MASSAGE<br>INTO SKIN UNDER<br>BEARD AREA AND<br>WORK OIL OUT TO-<br>WARDS BEARD. DIS-</p>
  <h1 class="label__title">BEARD OIL</h1>
  <div class="label__flavor">Tobacco Vanilla</div>
  <div class="label__heading label__heading--ingredients">Ingredients:</div>
  <p class="label__ingredients">FRACTIONATED COCONUT<br>OIL (MCT), GOLDEN<br>JOJOBA OIL. HEMP SEED<br>OIL, TEA TREE ESSENTIAL<br>OIL, ORANGE BITTER<br>ESSENTIAL OIL, PEPPER-<br>MINT SUPREME ESSENTIAL<br>OIL, TALLOW AROMAS.</p>
  <div class="label__dye">DYE FREE</div>
  <p class="label__origin">100%<br>MADE IN THE USA</p>
  <svg class="label__flag" viewBox="0 0 24 24"><defs><clipPath id="c4"><circle cx="12" cy="12" r="12"/></clipPath></defs><g clip-path="url(#c4)"><rect width="24" height="24" fill="#fff"/><rect y="0" width="24" height="3" fill="var(--flag-red)"/><rect y="6" width="24" height="3" fill="var(--flag-red)"/><rect y="12" width="24" height="3" fill="var(--flag-red)"/><rect y="18" width="24" height="3" fill="var(--flag-red)"/><rect width="11" height="12" fill="var(--flag-blue)"/></g></svg>
</section>

<section class="label label--forest">
  <svg class="label__band" viewBox="0 0 500 273"><polygon points="284,0 500,0 500,174 205,174" fill="var(--red)"/></svg>
  <div class="label__artwork" role="img" aria-label="Engraved portrait of a bearded man in a brimmed hat on kraft paper"></div>
  <div class="label__usa-box"></div>
  <div class="label__gold-strip"></div>
  <div class="label__size">~ 1 OZ ~</div>
  <div class="label__brand">Kinsmen<br>Crest</div>
  <div class="label__veteran">Veteran Owned Co.</div>
  <div class="label__heading label__heading--directions">Directions:</div>
  <p class="label__directions">APPLY 3-6 DROPS<br>INTO YOUR<br>HAND...RUB OIL INTO<br>HANDS AND APPLY<br>DIRECTLY ONTO<br>BEARD. FOR BEST<br>RESULTS MASSAGE<br>INTO SKIN UNDER<br>BEARD AREA AND<br>WORK OIL OUT TO-<br>WARDS BEARD. DIS-</p>
  <h1 class="label__title">BEARD OIL</h1>
  <div class="label__flavor">Tobacco Vanilla</div>
  <div class="label__heading label__heading--ingredients">Ingredients:</div>
  <p class="label__ingredients">FRACTIONATED COCONUT<br>OIL (MCT), GOLDEN<br>JOJOBA OIL. HEMP SEED<br>OIL, TEA TREE ESSENTIAL<br>OIL, ORANGE BITTER<br>ESSENTIAL OIL, PEPPER-<br>MINT SUPREME ESSENTIAL<br>OIL, TALLOW AROMAS.</p>
  <div class="label__dye">DYE FREE</div>
  <p class="label__origin">100%<br>MADE IN THE USA</p>
  <svg class="label__flag" viewBox="0 0 24 24"><defs><clipPath id="c5"><circle cx="12" cy="12" r="12"/></clipPath></defs><g clip-path="url(#c5)"><rect width="24" height="24" fill="#fff"/><rect y="0" width="24" height="3" fill="var(--flag-red)"/><rect y="6" width="24" height="3" fill="var(--flag-red)"/><rect y="12" width="24" height="3" fill="var(--flag-red)"/><rect y="18" width="24" height="3" fill="var(--flag-red)"/><rect width="11" height="12" fill="var(--flag-blue)"/></g></svg>
</section>

</body>
</html>
```